Marcus Lindqvist Photography needs a business card designs

I am looking for a business card with a logo clean and simple which I can use that logo on my website or on my pictures. It has to be very classy and very professional. Please look at my website at www.marcuslvqphoto.com for my signature. I'm thinking of something like that for my signature/logo. I'm still working on my website but you get an idea. I'm open to any design but not too busy graphics.

I will be printing the business card from qrivel.com.

Surprise me :)

contact me if you have any questions.

-ML

I'm receiving a lot of black background at the moment. I know my website is all black doesn't mean I want my card to be all black. Please send in with some white background as well. Thanks :)

check out some business cards that I found online. I think they are simple and look really awesome. I don't want a card that is too busy.

http://www.marcuslvqphoto.com/p270092084

Reason: Please extend the date for me. I haven't really receive any good design yet.

Printing

• -a logo that related to my first and last initial of my name "ML"
-double sided
• -I don't want my background to be all black.
-no pictures on the card

```html
<!DOCTYPE html>
<html lang="en">
<head>
<meta charset="utf-8">
<title>Marcus Lindqvist Photography – Business Card</title>
<link rel="stylesheet" href="https://fonts.googleapis.com/css2?family=Montserrat:wght@700;800;900&display=swap">
<style>
  :root {
    --page: #ffffff;
    --card-dark: #1c1e1f;
    --card-mid: #2d3031;
    --band-white: #ffffff;
    --band-edge: #e6e8e9;
    --brand-blue: #2f4cf5;
    --ink-dark: #222426;
    --bar-black: #111213;
    --rule: #9a9fa2;
  }
  * { margin: 0; padding: 0; box-sizing: border-box; }
  html, body {
    width: 1200px; height: 370px; overflow: hidden;
    background: var(--page);
    font-family: "Montserrat", Arial, sans-serif;
  }
  .sheet { position: relative; width: 1200px; height: 370px; }
  .card {
    position: absolute; top: 13px;
    width: 578px; height: 344px; overflow: hidden;
    background: radial-gradient(ellipse 80% 60% at 50% 50%, var(--card-mid), var(--card-dark) 100%);
  }
  .card--front { left: 11px; }
  .card--back { left: 606px; }

  .light-band { position: absolute; left: 0; top: 0; width: 578px; height: 344px; }

  .wordmark {
    position: absolute; text-align: center;
    color: var(--brand-blue); font-weight: 900; line-height: 1;
  }
  .wordmark__initials { display: block; letter-spacing: 2px; }
  .wordmark__sub { display: block; font-weight: 800; white-space: nowrap; }
  .wordmark__photo { color: var(--ink-dark); }
  .wordmark__graphy { color: var(--brand-blue); }

  .card--front .wordmark { left: 0; right: 0; top: 120px; }
  .card--front .wordmark__initials { font-size: 90px; }
  .card--front .wordmark__sub { font-size: 14px; letter-spacing: 7px; margin-top: 8px; }

  .name-bar {
    position: absolute; left: 50%; top: 231px; transform: translateX(-50%);
    width: 240px; height: 16px; background: var(--bar-black);
    color: var(--brand-blue); font-weight: 800; font-size: 12px;
    letter-spacing: 4.5px; text-align: center; line-height: 16px;
    white-space: nowrap;
  }

  .card--back .wordmark { left: 110px; width: 150px; top: 140px; }
  .card--back .wordmark__initials { font-size: 58px; }
  .card--back .wordmark__sub { font-size: 9.5px; letter-spacing: 3.5px; margin-top: 8px; }

  .divider {
    position: absolute; left: 272px; top: 145px;
    width: 1px; height: 52px; background: var(--rule);
  }
  .contact-list {
    position: absolute; left: 291px; top: 146px; list-style: none;
    color: var(--brand-blue); font-weight: 800; font-size: 11.5px;
    line-height: 14px; text-transform: uppercase; white-space: nowrap;
  }
  .contact-list li::before {
    content: "★"; color: var(--ink-dark); font-size: 8px;
    margin-right: 6px; position: relative; top: -1px;
  }
</style>
</head>
<body>
<div class="sheet">
  <section class="card card--front">
    <svg class="light-band" viewBox="0 0 578 344" aria-hidden="true">
      <defs>
        <linearGradient id="bandFront" x1="0" y1="0" x2="1" y2="0">
          <stop offset="0" stop-color="#e6e8e9"/>
          <stop offset="0.5" stop-color="#ffffff"/>
          <stop offset="1" stop-color="#e6e8e9"/>
        </linearGradient>
      </defs>
      <path d="M0 84 Q289 120 578 84 L578 262 Q289 226 578 262 Z" fill="none"/>
      <path d="M0 84 Q289 122 578 84 L578 264 Q289 226 0 264 Z" fill="url(#bandFront)"/>
    </svg>
    <div class="wordmark">
      <span class="wordmark__initials">ML</span>
      <span class="wordmark__sub"><span class="wordmark__photo">PHOTO</span><span class="wordmark__graphy">GRAPHY</span></span>
    </div>
    <div class="name-bar">MARCUS LINDQVIST</div>
  </section>

  <section class="card card--back">
    <svg class="light-band" viewBox="0 0 578 344" aria-hidden="true">
      <defs>
        <linearGradient id="bandBack" x1="0" y1="0" x2="1" y2="0">
          <stop offset="0" stop-color="#e6e8e9"/>
          <stop offset="0.5" stop-color="#ffffff"/>
          <stop offset="1" stop-color="#e6e8e9"/>
        </linearGradient>
      </defs>
      <path d="M0 96 Q289 132 578 96 L578 250 Q289 214 0 250 Z" fill="url(#bandBack)"/>
    </svg>
    <div class="wordmark">
      <span class="wordmark__initials">ML</span>
      <span class="wordmark__sub"><span class="wordmark__photo">PHOTO</span><span class="wordmark__graphy">GRAPHY</span></span>
    </div>
    <div class="divider"></div>
    <ul class="contact-list">
      <li>Marcus Lindqvist</li>
      <li>info@marcuslvqphoto.com</li>
      <li>555.014.2287</li>
      <li>www.marcuslvqphoto.com</li>
    </ul>
  </section>
</div>
</body>
</html>
```